Boring Fiberglass Repair Company needs creative business cards

The Fiberglass Repair industry isn't very fun or creative but we'd like a business card that communicates a fresh, modern, and service-oriented feel. We repair bathroom fixtures (bath tubs, showers, etc) which are made out of fiberglass. Our fiberglass repair service will be sold to bathtub manufacturers and also businesses that sell bathtubs. We will also offer our services to home owners that have broken showers and bathtubs.
Target Market(s)
Home builders, plumbing wholesalers, home owners
Contact Information for Business Card
Name
Phone Number
Email Address
Business Address
Tag line: "Quality Craftsmanship Today"

```html
<!DOCTYPE html>
<html lang="en">
<head>
<meta charset="utf-8">
<title>Mesa Ridge Fiberglass – Business Cards</title>
<link rel="stylesheet" href="https://fonts.googleapis.com/css2?family=Montserrat:wght@500;600;800&family=Open+Sans:wght@400;600&display=swap">
<style>
  :root {
    --navy: #1f2d5e;
    --navy-deep: #18234c;
    --red: #c42430;
    --white: #ffffff;
    --backdrop: #e9e7e3;
    --rule: rgba(255,255,255,0.35);
  }
  * { margin: 0; padding: 0; box-sizing: border-box; }
  html, body {
    width: 1200px; height: 900px; overflow: hidden;
    background: var(--backdrop);
  }
  .canvas { position: relative; width: 1200px; height: 900px; }
  .card {
    position: absolute; left: 270px; width: 660px; height: 377px;
    overflow: hidden; border-radius: 4px;
    box-shadow: 0 8px 22px rgba(0,0,0,0.22);
  }
  .card-back {
    top: 50px;
    background: linear-gradient(160deg, #243468 0%, var(--navy) 55%, var(--navy-deep) 100%);
    color: var(--white);
    text-align: center;
  }
  .brand-name {
    font-family: "Montserrat", sans-serif;
    font-weight: 800;
    letter-spacing: 1px;
  }
  .card-back .brand-name {
    position: absolute; top: 128px; left: 0; right: 0;
    font-size: 34px; color: var(--white);
  }
  .card-back .rule {
    position: absolute; top: 212px; left: 80px; right: 80px;
    height: 1px; background: var(--rule);
  }
  .tagline {
    position: absolute; top: 232px; left: 0; right: 0;
    font-family: "Montserrat", sans-serif; font-weight: 600;
    font-size: 22px; letter-spacing: 3px; color: var(--white);
  }
  .card-front { top: 470px; background: var(--white); }
  .card-front .art { position: absolute; inset: 0; }
  .card-front .brand-name {
    position: absolute; top: 34px; left: 356px;
    font-size: 30px; line-height: 1.1; color: var(--navy);
  }
  .person { position: absolute; top: 78px; left: 28px; color: var(--white); }
  .person-role { font-family: "Open Sans", sans-serif; font-size: 17px; font-weight: 400; }
  .person-name {
    font-family: "Montserrat", sans-serif; font-weight: 800; font-size: 27px; line-height: 1.05;
  }
  .contacts {
    position: absolute; left: 28px; bottom: 26px; width: 380px;
    font-family: "Open Sans", sans-serif; color: var(--white);
  }
  .contact {
    display: flex; align-items: center; gap: 12px;
    font-size: 18px; line-height: 30px;
  }
  .contact svg { width: 16px; height: 16px; flex: none; fill: var(--white); }
  .contact-address { font-size: 16px; }
  .contacts .rule { height: 1px; background: rgba(255,255,255,0.5); margin: 8px 0 6px; }
</style>
</head>
<body>
<main class="canvas">

  <section class="card card-back" aria-label="Card back">
    <div class="brand-name">MESA RIDGE FIBERGLASS</div>
    <div class="rule"></div>
    <p class="tagline">Quality Craftsmanship Today</p>
  </section>

  <section class="card card-front" aria-label="Card front">
    <svg class="art" viewBox="0 0 660 377" preserveAspectRatio="none">
      <defs>
        <linearGradient id="facet-tone" x1="0" y1="0" x2="0.8" y2="1">
          <stop offset="0" stop-color="#b9495f"/>
          <stop offset="0.45" stop-color="#8a6f92"/>
          <stop offset="1" stop-color="#4f5f93"/>
        </linearGradient>
      </defs>
      <rect width="660" height="377" fill="url(#facet-tone)" role="img" aria-label="Faceted geometric background in rose and slate blue"/>
      <polygon points="178,0 200,0 230,45 660,305 660,332 212,60" fill="var(--red)"/>
      <polygon points="200,0 660,0 660,305 230,45" fill="var(--white)"/>
    </svg>

    <div class="brand-name">MESA RIDGE<br>FIBERGLASS</div>

    <div class="person">
      <p class="person-role">Director</p>
      <p class="person-name">JOHN DOE</p>
    </div>

    <div class="contacts">
      <p class="contact">
        <svg viewBox="0 0 24 24" aria-hidden="true"><path d="M6.6 10.8a15 15 0 0 0 6.6 6.6l2.2-2.2a1 1 0 0 1 1-.25 11.4 11.4 0 0 0 3.6.57 1 1 0 0 1 1 1V20a1 1 0 0 1-1 1A17 17 0 0 1 3 4a1 1 0 0 1 1-1h3.5a1 1 0 0 1 1 1c0 1.25.2 2.45.57 3.57a1 1 0 0 1-.25 1z"/></svg>
        1234 5678 90
      </p>
      <p class="contact">
        <svg viewBox="0 0 24 24" aria-hidden="true"><path d="M3 5h18v14H3zm2 2v.5l7 4.5 7-4.5V7zm0 2.8V17h14V9.8l-7 4.5z"/></svg>
        info@mesaridgefiberglass.com
      </p>
      <div class="rule"></div>
      <p class="contact contact-address">
        <svg viewBox="0 0 24 24" aria-hidden="true"><path d="M12 2a7 7 0 0 0-7 7c0 5 7 13 7 13s7-8 7-13a7 7 0 0 0-7-7zm0 9.5A2.5 2.5 0 1 1 12 6.5a2.5 2.5 0 0 1 0 5z"/></svg>
        99 dummy city, dummy place, Dummy Land
      </p>
    </div>
  </section>

</main>
</body>
</html>
```